Men’s hair skin and beard line

I own a men’s salon in Texas and are beginning to expand its market into the men’s retail line and already have it being manufactured out of the UK. It’s paraben free, vegan, sulphate free. I need a better brand look for the packaging. This script font is a bit hard to read. I want it masculine yet clean lines. All colors even gold or silver are welcomed. Bottle choices are silver canisters, white or black.

Target Market(s)

Men

Industry/Entity Type

Men’s hair skin and beard industry. Retail centers, high end barbers, and gyms

Font styles to use
Other font styles liked:
• Montserrat ,helvetica neue, or lato font

Colors
0054AA
0677BA
7BADD7
CADEEF
E8F1F8
0094D4
00A9DD
6FCCEA
C7EBF8
E9F6FB
00AB8E
00BBA5
67D7C9
C6EFE9
E9F9F6

Requirements
Must have
• Logo and name
Nice to have
• I’m open to all.
Should not have
• Not feminine

```html
<!DOCTYPE html>
<html lang="en">
<head>
<meta charset="utf-8">
<title>Stratum Men's Fine Grooming – Label Set</title>
<link href="https://fonts.googleapis.com/css2?family=Montserrat:wght@700;800&family=Roboto:wght@400;700&display=swap" rel="stylesheet">
<style>
  :root{
    --gold:#c9a24a;
    --gold-light:#e6c97a;
    --gold-dark:#9c7a2c;
    --blue:#1457a8;
    --black:#000000;
    --paper:#f2f2f4;
    --ink:#111111;
    --white:#ffffff;
    --frame:#8a8a8a;
    --beard-light:#ffffff;
    --beard-dark:#111111;
  }
  *{box-sizing:border-box;margin:0;padding:0}
  html,body{width:1200px;height:274px;overflow:hidden;background:var(--white)}
  .sheet{position:relative;width:1200px;height:274px}
  .label{position:absolute;top:0;width:140px;height:274px;text-align:center;font-family:"Roboto",Arial,sans-serif}
  .label--black{background:var(--black);color:var(--white)}
  .label--blue{background:var(--blue);color:var(--white)}
  .label--paper{background:var(--paper);color:var(--ink);border:0.6px solid var(--frame)}

  .brand{position:absolute;top:70px;left:0;right:0}
  .brand__mark{display:block;width:10px;height:10px;border-radius:50%;margin:0 auto 6px;background:currentColor}
  .brand__name{font-family:"Montserrat",Arial,sans-serif;font-weight:800;font-size:17px;letter-spacing:0.3px;line-height:1}
  .brand__tag{font-family:"Montserrat",Arial,sans-serif;font-weight:700;font-size:5.2px;letter-spacing:0.3px;margin-top:3px}
  .brand__tag::before,.brand__tag::after{content:"";display:inline-block;width:6px;height:0.8px;background:currentColor;vertical-align:middle;margin:0 3px}
  .tone-gold{color:var(--gold)}
  .tone-ink{color:var(--ink)}
  .tone-blue{color:var(--blue)}

  .title{position:absolute;left:0;right:0;font-weight:400;font-size:21.5px;line-height:20px;letter-spacing:-0.2px}
  .title--cleanser{top:117px}
  .title--oil{top:178px}

  .band{position:absolute;top:158px;left:0;right:0;height:11px;font-weight:700;font-size:7px;line-height:11px;letter-spacing:0.2px}
  .band--gold{background:linear-gradient(90deg,var(--gold-dark),var(--gold-light) 50%,var(--gold-dark));color:var(--ink)}
  .band--blue{background:var(--blue);color:var(--white)}

  .copy{position:absolute;top:174px;left:8px;right:8px;font-size:5.6px;line-height:6.6px}

  .subtitle{position:absolute;top:202px;left:0;right:0;font-weight:700;font-size:7px;letter-spacing:0.2px}

  .art{position:absolute;top:116px;left:47px;width:46px;height:60px;border-radius:20px 20px 22px 22px}
  .art--light{background:var(--beard-light)}
  .art--dark{background:var(--beard-dark)}

  .seal{position:absolute;top:223px;left:51px;width:38px;height:38px;border-radius:50%}
  .seal--gold{background:radial-gradient(circle,var(--gold-light),var(--gold) 70%,var(--gold-dark))}
  .seal--black{background:var(--black);border:3px solid var(--paper);box-shadow:0 0 0 1.5px var(--black)}
  .seal--blue{background:var(--blue);border:3px solid var(--paper);box-shadow:0 0 0 1.5px var(--blue)}

  .volume{position:absolute;top:262px;left:0;right:0;font-size:5px}
  .volume--faint{color:#c9c9c9}
</style>
</head>
<body>
<main class="sheet">

  <!-- Facial cleanser: black / gold -->
  <section class="label label--black" style="left:12px">
    <div class="brand tone-gold"><span class="brand__mark"></span><div class="brand__name">STRATUM</div><div class="brand__tag">MEN'S FINE GROOMING</div></div>
    <h2 class="title title--cleanser">FACIAL<br>CLEANSAR</h2>
    <div class="band band--gold">POST WASH FACIAL CLEANSER</div>
    <p class="copy">Enriched with organic Aloe Vera that gently cleanses the surface oil and impurities from your skin, while body your face hydrated and rejoice</p>
    <div class="seal seal--gold" role="img" aria-label="Cruelty free vegan product seal"></div>
    <p class="volume">100ml/3.4floz</p>
  </section>

  <!-- Facial cleanser: white / gold band -->
  <section class="label label--paper" style="left:168px">
    <div class="brand tone-ink"><span class="brand__mark"></span><div class="brand__name">STRATUM</div><div class="brand__tag">MEN'S FINE GROOMING</div></div>
    <h2 class="title title--cleanser">FACIAL<br>CLEANSAR</h2>
    <div class="band band--gold">POST WASH FACIAL CLEANSER</div>
    <p class="copy">Enriched with organic Aloe Vera that gently cleanses the surface oil and impurities from your skin, while body your face hydrated and rejoice</p>
    <div class="seal seal--black" role="img" aria-label="Cruelty free vegan product seal"></div>
    <p class="volume">100ml/3.4floz</p>
  </section>

  <!-- Facial cleanser: white / blue -->
  <section class="label label--paper" style="left:323px">
    <div class="brand tone-blue"><span class="brand__mark"></span><div class="brand__name">STRATUM</div><div class="brand__tag">MEN'S FINE GROOMING</div></div>
    <h2 class="title title--cleanser">FACIAL<br>CLEANSAR</h2>
    <div class="band band--blue">POST WASH FACIAL CLEANSER</div>
    <p class="copy">Enriched with organic Aloe Vera that gently cleanses the surface oil and impurities from your skin, while body your face hydrated and rejoice</p>
    <div class="seal seal--blue" role="img" aria-label="Cruelty free vegan product seal"></div>
    <p class="volume">100ml/3.4floz</p>
  </section>

  <!-- Beard oil: blue -->
  <section class="label label--blue" style="left:494px">
    <div class="brand tone-gold"><span class="brand__mark"></span><div class="brand__name">STRATUM</div><div class="brand__tag">MEN'S FINE GROOMING</div></div>
    <div class="art art--light" role="img" aria-label="Illustration of a bearded man's head"></div>
    <h2 class="title title--oil">BEARD OIL</h2>
    <p class="subtitle">AROMA FRAGRANCE</p>
    <div class="seal seal--gold" role="img" aria-label="Cruelty free vegan product seal"></div>
    <p class="volume">100ml/3.4floz</p>
  </section>

  <!-- Beard oil: black -->
  <section class="label label--black" style="left:651px">
    <div class="brand tone-gold"><span class="brand__mark"></span><div class="brand__name">STRATUM</div><div class="brand__tag">MEN'S FINE GROOMING</div></div>
    <div class="art art--light" role="img" aria-label="Illustration of a bearded man's head"></div>
    <h2 class="title title--oil">BEARD OIL</h2>
    <p class="subtitle">AROMA FRAGRANCE</p>
    <div class="seal seal--gold" role="img" aria-label="Cruelty free vegan product seal"></div>
    <p class="volume">100ml/3.4floz</p>
  </section>

  <!-- Beard oil: white -->
  <section class="label label--paper" style="left:816px">
    <div class="brand tone-ink"><span class="brand__mark"></span><div class="brand__name">STRATUM</div><div class="brand__tag">MEN'S FINE GROOMING</div></div>
    <div class="art art--dark" role="img" aria-label="Illustration of a bearded man's head"></div>
    <h2 class="title title--oil">BEARD OIL</h2>
    <p class="subtitle">AROMA FRAGRANCE</p>
    <div class="seal seal--gold" role="img" aria-label="Cruelty free vegan product seal"></div>
    <p class="volume volume--faint">100ml/3.4floz</p>
  </section>

</main>
</body>
</html>
```